IT Network Consultancy - Business Card

t4 linkways is a IT network consultancy based in London. We're looking for a smart, modern and professional business card design. Our website is here: www.t4linkways.co.uk

Key things that should be included on the card (with examples):

Company Logo
Name
Position / Job Title: Network Consultant
Mobile Phone Number: +44 (0) 7700 900418
Land Line: +44 (0) 1632 960274
Email Address: name@t4linkways.co.uk
Web Site URL: www.t4linkways.co.uk

Target Market(s)

Large enterprise / global companies / corporates

Industry/Entity Type

Business

Requirements
Must have
• Incorporate our logo - which is attached to the project. They are in AI format (can be opened in Inkscape).

The design should be double sided and fit on a UK standard 85mm × 55mm card and be in a format that retains the quality when printed.
Nice to have
• The project does not have to conform to the colour of our website but this should give you inspiration of the style we like.
Should not have
• Bright colours. Pictures are not necessary.

```html
<!DOCTYPE html>
<html lang="en">
<head>
<meta charset="utf-8">
<title>t4 linkways – Business Card</title>
<link rel="stylesheet" href="https://fonts.googleapis.com/css2?family=PT+Sans:ital,wght@0,400;0,700;1,400&display=swap">
<style>
  :root {
    --page-bg: #e4e4e6;
    --front-dark: #3c424b;
    --front-mid: #525a64;
    --front-band: #2b2f35;
    --logo-light: #8f99a4;
    --back-light: #f7f7f8;
    --back-shade: #dcdcde;
    --name-band: #2e3238;
    --ink: #2f3338;
    --white: #ffffff;
  }
  * { box-sizing: border-box; margin: 0; padding: 0; }
  html, body {
    width: 1200px; height: 765px; overflow: hidden;
    background: var(--page-bg);
    font-family: "PT Sans", Arial, sans-serif;
  }
  .card {
    position: absolute; top: 302px;
    width: 574px; height: 344px;
    border-radius: 36px; overflow: hidden;
  }
  .card--front { left: 16px; background: var(--front-dark); }
  .card--back {
    left: 604px;
    background: linear-gradient(160deg, var(--back-light) 0%, #ededee 55%, var(--back-shade) 100%);
    border: 1px solid #c9c9cc;
  }
  .front-texture {
    position: absolute; inset: 0;
    background: linear-gradient(150deg, #56606b 0%, #434a53 45%, #383d45 100%);
  }
  .front-rule {
    position: absolute; left: 0; top: 157px;
    width: 150px; height: 24px;
    background: var(--front-band);
    border-top: 1px solid #6a727c;
  }
  .front-logo {
    position: absolute; left: 60px; top: 78px;
    color: var(--logo-light); font-weight: 400; line-height: 1;
  }
  .front-logo .logo-mark { display: block; font-size: 104px; letter-spacing: -2px; }
  .front-logo .logo-word { display: block; font-size: 46px; letter-spacing: 3px; margin-top: 4px; }

  .back-logo {
    position: absolute; left: 236px; top: 94px;
    font-size: 34px; color: var(--ink); letter-spacing: 1px; line-height: 1;
  }
  .name-band {
    position: absolute; left: 230px; right: 0; top: 154px; height: 30px;
    background: var(--name-band);
    border: 1px solid #8a8e94; border-right: none;
    display: flex; align-items: center; padding-left: 8px; color: var(--white);
  }
  .name-band .person { font-size: 21px; }
  .name-band .role { font-style: italic; font-size: 14px; margin-left: 30px; margin-top: 3px; }
  .contact {
    position: absolute; left: 236px; top: 195px;
    list-style: none; font-size: 13.5px; color: var(--ink); line-height: 20px;
  }
  .contact strong { font-weight: 700; }
  .website {
    position: absolute; left: 236px; top: 264px;
    font-size: 14px; letter-spacing: 5.3px; color: var(--ink);
  }
</style>
</head>
<body>
  <section class="card card--front" aria-label="Card front">
    <div class="front-texture" role="img" aria-label="Muted blurred grey-blue background imagery"></div>
    <div class="front-rule"></div>
    <div class="front-logo">
      <span class="logo-mark">t4</span>
      <span class="logo-word">linkways</span>
    </div>
  </section>

  <section class="card card--back" aria-label="Card back">
    <div class="back-logo">t4 linkways</div>
    <div class="name-band">
      <span class="person">Daniel Marsh</span>
      <span class="role">Network Consultant</span>
    </div>
    <ul class="contact">
      <li>Mobile Phone Number: <strong>+44 (0) 7700 900418</strong></li>
      <li>Land Line: <strong>+44 (0) 1632 960274</strong></li>
      <li>Email Address: <strong>name@t4linkways.co.uk</strong></li>
    </ul>
    <div class="website">www.t4linkways.co.uk</div>
  </section>
</body>
</html>
```